Postcard Design for Licensed Financial Agent

I want a postcard designed to be more like a flyer and a business card combined. This is to draw the attention of individual searching for or have overlooked the need in their lives for life insurance. Right now I am not very sure what size postcard will work best for this project so I selected medium. . I am a licensed agent and I have worked on some ideals of the basics that I would like to have but want your professional input on making this product successfully. My business cards were created by Crestmarkly and I would like to have that information on the back of the postcard.

On one side I want the information from the attachment from the insurance interest postcard document that I attempted to create.

On the other side of the postcard I would like the information from my business card you printed for me on August 28 of 2014. The box number reads K 47316025581904 K72 at the bottom of the bar code it has TW83. If there is any other information you need to get the business card information you printed for me previously please contact me with any questions so we together can get this project on its way. Thank you for your attention to this matter. Oralie Funston

Industry/Entity Type

Business

Requirements
Must have
• Text for front: IF YOU EXPERIENCED THE SUDDEN LOST OF A LOVED ONE CAN YOU IMMEDIATELY PROVIDE THE COST OF FINAL EXPENSE?*

```html
<!DOCTYPE html>
<html lang="en">
<head>
<meta charset="utf-8">
<title>Life Insurance Postcard – Oralie Funston</title>
<link rel="stylesheet" href="https://fonts.googleapis.com/css2?family=Oswald:wght@600;700&family=Lato:wght@400;700;900&display=swap">
<style>
  :root {
    --navy: #0b2a6b;
    --navy-deep: #08245f;
    --blue-stripe: #1e4bb0;
    --green: #1aa861;
    --white: #ffffff;
    --ink-grey: #3a3a3a;
    --page: #eeeeee;
    --rule: #9a9a9a;
    --frame: #222222;
  }
  * { margin: 0; padding: 0; box-sizing: border-box; }
  html, body { width: 900px; height: 1200px; overflow: hidden; background: var(--page); }
  .canvas { position: relative; width: 900px; height: 1200px; }

  .postcard { position: absolute; overflow: hidden; background: var(--white); }
  .postcard > svg { position: absolute; inset: 0; display: block; }
  .postcard-front { left: 110px; top: 70px; width: 685px; height: 492px; }
  .postcard-back  { left: 113px; top: 638px; width: 682px; height: 490px; }

  .headline {
    position: absolute; left: 25px; top: 14px;
    font-family: "Oswald", "Arial Narrow", sans-serif; font-weight: 700;
    font-size: 36px; line-height: 43px; color: var(--white); letter-spacing: 0.6px;
  }
  .headline .accent { color: var(--green); }

  .question {
    position: absolute; left: 25px; top: 173px;
    font-family: "Lato", Arial, sans-serif; font-size: 18.5px; line-height: 24px;
    color: var(--ink-grey); letter-spacing: 1px; word-spacing: 2px;
  }
  .question-strong {
    position: absolute; left: 25px; top: 221px;
    font-family: "Lato", Arial, sans-serif; font-weight: 900; font-size: 24.5px; line-height: 30px;
    color: var(--navy);
  }
  .question-footer {
    position: absolute; left: 55px; top: 385px;
    font-family: "Lato", Arial, sans-serif; font-size: 19px; line-height: 26px;
    color: var(--white); letter-spacing: 0.4px;
  }

  .agent-name {
    position: absolute; left: 19px; top: 206px;
    font-family: "Lato", Arial, sans-serif; font-weight: 700; font-size: 27px;
    color: var(--white); white-space: nowrap;
  }
  .agent-pitch {
    position: absolute; left: 19px; top: 240px;
    font-family: "Lato", Arial, sans-serif; font-size: 16px; line-height: 20px;
    color: var(--white);
  }
</style>
</head>
<body>
<main class="canvas">

  <section class="postcard postcard-front" aria-label="Postcard front">
    <svg width="685" height="492" viewBox="0 0 685 492">
      <defs>
        <linearGradient id="mistGrad" x1="0" y1="0" x2="1" y2="0">
          <stop offset="0" stop-color="#f1f1f2"/>
          <stop offset="0.5" stop-color="#dfe0e2"/>
          <stop offset="1" stop-color="#ecedee"/>
        </linearGradient>
        <linearGradient id="callerGrad" x1="0" y1="0" x2="1" y2="1">
          <stop offset="0" stop-color="#d9d3c8"/>
          <stop offset="0.5" stop-color="#c4a98a"/>
          <stop offset="1" stop-color="#e8e4dc"/>
        </linearGradient>
        <linearGradient id="agentGrad" x1="0" y1="0" x2="0" y2="1">
          <stop offset="0" stop-color="#f4f2ef"/>
          <stop offset="0.55" stop-color="#c8a58a"/>
          <stop offset="1" stop-color="#8e9cc3"/>
        </linearGradient>
      </defs>
      <rect class="backdrop-photo" x="0" y="0" width="685" height="492" fill="url(#mistGrad)" role="img" aria-label="Faded photo of a grieving woman in the background"/>
      <rect class="headline-band" x="0" y="0" width="685" height="160" fill="var(--navy)"/>
      <path class="accent-stripe" d="M355 0 C380 40 410 110 470 150 C540 195 620 195 685 188 V205 C610 212 520 210 455 165 C400 125 375 45 345 0 Z" fill="var(--blue-stripe)"/>
      <path class="photo-caller" d="M362 0 H685 V182 C610 190 540 185 480 145 C420 105 390 45 362 0 Z" fill="url(#callerGrad)" stroke="var(--white)" stroke-width="3" role="img" aria-label="Photo of a distressed woman on the phone"/>
      <path class="wave-green" d="M0 330 C60 295 130 282 200 285 C300 290 400 350 500 390 L685 355 V492 H0 Z" fill="var(--green)"/>
      <path class="wave-white" d="M0 344 C60 309 130 296 200 299 C300 304 400 364 500 404 L685 369 V492 H0 Z" fill="var(--white)"/>
      <path class="wave-navy" d="M0 354 C60 320 130 308 200 311 C300 316 400 376 500 416 L685 381 V492 H0 Z" fill="var(--navy)"/>
      <circle class="portrait-ring-green" cx="562" cy="364" r="98" fill="var(--green)"/>
      <circle class="portrait-ring-white" cx="562" cy="364" r="86" fill="var(--white)"/>
      <circle class="portrait-ring-navy" cx="562" cy="364" r="82" fill="var(--navy)"/>
      <circle class="portrait-agent" cx="562" cy="364" r="73" fill="url(#agentGrad)" role="img" aria-label="Portrait of the agent, Oralie Funston"/>
    </svg>
    <h1 class="headline">IF YOU EXPERIENCED<br>THE SUDDEN LOST OF A<br><span class="accent">LOVED ONE CAN YOU</span></h1>
    <p class="question">IS THE ONLY LIFE INSURANCE COVERAGE YOU<br>HAVE PROVIDED THROUGH AN EMPLOYER?</p>
    <p class="question-strong">HAVE YOU HAD DIFFICUTLTIES GETTING<br>INSURANCE COVERAGE IN THE PAST?</p>
    <p class="question-footer">HAVE YOU HAD DIFFICUTLTIES<br>GETTING INSURANCE<br>COVERAGE IN THE PAST?</p>
  </section>

  <section class="postcard postcard-back" aria-label="Postcard back">
    <svg width="682" height="490" viewBox="0 0 682 490">
      <defs>
        <linearGradient id="thinkerGrad" x1="0" y1="0" x2="1" y2="0">
          <stop offset="0" stop-color="#b89a80"/>
          <stop offset="0.5" stop-color="#d8c6b4"/>
          <stop offset="1" stop-color="#f2f4f3"/>
        </linearGradient>
      </defs>
      <path class="stripe-green" d="M342 0 H380 C405 80 385 170 350 260 C320 340 290 420 275 490 H240 C260 420 290 340 320 260 C355 170 372 80 342 0 Z" fill="var(--green)"/>
      <path class="panel-navy" d="M0 0 H342 C372 80 355 170 320 260 C290 340 260 420 240 490 H0 Z" fill="var(--navy)"/>
      <path class="photo-border-green" d="M0 0 H352 C345 80 310 140 220 160 C140 176 50 168 0 145 Z" fill="var(--green)"/>
      <path class="photo-border-white" d="M0 0 H340 C333 74 300 130 215 148 C140 163 50 155 0 133 Z" fill="var(--white)"/>
      <path class="photo-thinker" d="M0 0 H332 C325 70 292 124 212 140 C140 154 50 147 0 126 Z" fill="url(#thinkerGrad)" role="img" aria-label="Photo of a thoughtful woman by a window"/>
      <path class="contact-box" d="M0 405 H223 Q243 405 243 425 V457 Q243 477 223 477 H0 Z" fill="var(--green)"/>
      <rect class="stamp-box" x="573.5" y="17.5" width="91" height="91" fill="none" stroke="var(--frame)" stroke-width="1"/>
      <g class="address-lines" stroke="var(--rule)" stroke-width="1">
        <line x1="405" y1="250.5" x2="622" y2="250.5"/>
        <line x1="405" y1="299.5" x2="622" y2="299.5"/>
        <line x1="407" y1="355.5" x2="623" y2="355.5"/>
      </g>
    </svg>
    <h2 class="agent-name">LET ORALIE FUNSTON</h2>
    <p class="agent-pitch">ASSIST YOU TO RESEARCH<br>INTELLIFENT FINANCIAL<br>SOLUTIONS TO PROVIDE<br>YOU THE HELP YOU NEED</p>
  </section>

</main>
</body>
</html>
```